Natural Stone Company Redesign

Looking for a fresh, creative, website design. We service Luxury Residential projects in US and Internationally. We would like to see a design that communicates a passion for creative challenging design that is merged with natural stone projects. Our new company Logo is "Stoneleaf Atelier"

We like to emphasis from concept to completion, for example, photos of blueprints and/or sketches of a project, then a completion photo of same project.

some websites we like are:
http://www.fernbrockhale.com/
http://lontavimarchitects.com/

We would like to highlight our services of "concept to completion" scenario. Blueprints/sketches to finished products.
Page needed:
Home
About Us
Projects
Contact Us

Target Market(s)

Developers, architects, designers

Industry/Entity Type

It Company

Number of Pages Required

4 page

Font styles to use
Sans Serif

Requirements
Must have
• "Stoneleaf Atelier"
• New, innovative, look.
• Something to grab the attention, and make them think
Nice to have
• Motion on the homepage
• Roll over the finished project photo, and have the name of the stone pop up

```html
<!DOCTYPE html>
<html lang="en">
<head>
<meta charset="utf-8">
<title>Our Projects – Stoneleaf Atelier</title>
<link href="https://fonts.googleapis.com/css2?family=Poppins:wght@300;400;500&family=Roboto:ital,wght@0,400;1,400&display=swap" rel="stylesheet">
<style>
  :root{
    --ink:#2b2f3a;
    --navy:#262b3b;
    --navy-line:#3a4052;
    --accent:#f07a2c;
    --muted:#b7bcc8;
    --white:#ffffff;
    --grey-text:#555a66;
  }
  *{margin:0;padding:0;box-sizing:border-box}
  html,body{width:719px;height:1200px;overflow:hidden;background:var(--white)}
  body{position:relative;font-family:"Poppins",sans-serif;color:var(--ink)}
  a{color:inherit;text-decoration:none}
  .abs{position:absolute}
  .site-header{left:0;top:0;width:719px;height:46px;background:var(--white)}
  .brand{left:53px;top:13px;font-size:14px;font-weight:400;line-height:20px;color:var(--ink)}
  .menu-toggle{left:654px;top:17px}
  .hero{left:0;top:46px;width:719px;height:118px;
    background:linear-gradient(90deg,#5c6070 0%,#7b7a7a 35%,#8d8579 55%,#6a6b72 75%,#a9aab0 100%)}
  .hero::after{content:"";position:absolute;inset:0;background:rgba(40,44,60,.35)}
  .hero-title{left:0;width:719px;top:86px;text-align:center;color:var(--white);font-size:22px;font-weight:300;line-height:30px;z-index:1}
  .breadcrumb{left:0;width:719px;top:120px;text-align:center;color:var(--white);font-family:"Roboto",sans-serif;font-size:7.5px;line-height:10px;z-index:1;letter-spacing:.2px}
  .breadcrumb span{margin:0 6px}
  .section-num{left:52px;top:202px;font-size:28px;font-weight:300;line-height:36px;color:var(--ink)}
  .section-rule{left:53px;top:243px;width:2px;height:42px;background:var(--accent)}
  .section-title{left:69px;top:246px;font-size:16.5px;font-weight:300;line-height:21px;color:var(--ink)}
  .project{width:183px;height:197px;overflow:hidden}
  .project .photo{position:absolute;inset:0}
  .project .shade{position:absolute;inset:0;background:linear-gradient(180deg,rgba(0,0,0,0) 45%,rgba(20,22,30,.45) 100%)}
  .project .name{position:absolute;left:0;width:100%;top:143px;text-align:center;color:var(--white);font-size:12px;font-weight:400;line-height:16px}
  .project .place{position:absolute;left:0;width:100%;top:160px;text-align:center;color:#e4e4e8;font-family:"Roboto",sans-serif;font-style:italic;font-size:7px;line-height:9px}
  .pager{top:976px;font-family:"Roboto",sans-serif;font-size:7.5px;line-height:10px;font-weight:400;color:var(--grey-text)}
  .pager-active{left:348px;top:970px;width:25px;height:20px;border-radius:10px;background:var(--navy);box-shadow:0 2px 4px rgba(0,0,0,.25)}
  .pager-active-num{color:var(--white)}
  .site-footer{left:0;top:1016px;width:719px;height:184px;background:var(--navy)}
  .footer-heading{top:1056px;color:var(--white);font-size:11px;font-weight:400;line-height:15px}
  .footer-rule{top:1075px;width:14px;height:1.5px;background:var(--accent)}
  .footer-item{font-family:"Roboto",sans-serif;font-size:7px;line-height:10px;font-weight:400;color:var(--muted)}
  .news-input{left:475px;top:1090px;width:191px;height:18px;border-bottom:1px solid var(--muted);font-family:"Roboto",sans-serif;font-size:8px;color:#9aa0ad;padding-top:2px}
  .news-button{left:476px;top:1118px;width:26px;height:16px;border-radius:8px;background:var(--accent)}
  .footer-divider{left:53px;top:1168px;width:613px;height:1px;background:var(--navy-line)}
  .copyright{left:53px;top:1179px;font-family:"Roboto",sans-serif;font-size:7px;line-height:10px;font-weight:400;color:var(--white)}
  .to-top{left:681px;top:1156px;width:24px;height:24px;border-radius:12px;background:#3a3f4f}
</style>
</head>
<body>
  <header class="site-header abs">
    <div class="brand abs">Stoneleaf Atelier</div>
    <svg class="menu-toggle abs" width="12" height="11" viewBox="0 0 12 11"><path d="M0 1h12M0 5.5h12M0 10h12" stroke="#2b2f3a" stroke-width="1.2"/></svg>
  </header>

  <section class="hero abs" role="img" aria-label="Photo of a modern stone-clad house at dusk"></section>
  <h1 class="hero-title abs">Our Projects</h1>
  <div class="breadcrumb abs">HOME<span>›</span>OUR PROJECTS</div>

  <div class="section-num abs">01</div>
  <div class="section-rule abs"></div>
  <h2 class="section-title abs">Concept<br>to Completion</h2>

  <a class="project abs" style="left:53px;top:316px">
    <div class="photo" role="img" aria-label="Photo of a two-storey suburban house at twilight" style="background:linear-gradient(180deg,#8a86b8 0%,#6c6fa2 40%,#4a4f86 70%,#3c4275 100%)"></div>
    <div class="shade"></div><div class="name">Project 1 name</div><div class="place">Australia</div>
  </a>
  <a class="project abs" style="left:53px;top:529px">
    <div class="photo" role="img" aria-label="Photo of a flat-roofed modern home with a lawn" style="background:linear-gradient(180deg,#d9dde0 0%,#b9b8b0 40%,#5d5e4a 70%,#3e4a30 100%)"></div>
    <div class="shade"></div><div class="name">Project 4 name</div><div class="place">Kenia</div>
  </a>
  <a class="project abs" style="left:53px;top:742px">
    <div class="photo" role="img" aria-label="Photo of a timber deck beside a snowy forest" style="background:linear-gradient(90deg,#3e3a3a 0%,#5a4d47 45%,#a9a7a6 75%,#c9c8c6 100%)"></div>
    <div class="shade"></div><div class="name">Project 7 name</div><div class="place">Hongkong</div>
  </a>

  <a class="project abs" style="left:269px;top:262px">
    <div class="photo" role="img" aria-label="Photo of a wooden house among misty trees" style="background:linear-gradient(180deg,#8b8a86 0%,#5f5a50 45%,#53423c 75%,#3e3534 100%)"></div>
    <div class="shade"></div><div class="name">Project 2 name</div><div class="place">Italy</div>
  </a>
  <a class="project abs" style="left:269px;top:475px">
    <div class="photo" role="img" aria-label="Photo of a Tudor-style house with a tiled roof" style="background:linear-gradient(180deg,#6fb0d4 0%,#9cc6dc 30%,#a4533a 55%,#6c4a3a 80%,#5b4838 100%)"></div>
    <div class="shade"></div><div class="name">Project 5 name</div><div class="place">UAE</div>
  </a>
  <a class="project abs" style="left:269px;top:689px">
    <div class="photo" role="img" aria-label="Photo of a modern timber-clad townhouse" style="background:linear-gradient(180deg,#7fc0e0 0%,#a6d2e6 25%,#a5805f 50%,#7a6550 75%,#4a4a3e 100%)"></div>
    <div class="shade"></div><div class="name">Project 8 name</div><div class="place">Thailand</div>
  </a>

  <a class="project abs" style="left:483px;top:210px">
    <div class="photo" role="img" aria-label="Photo of a lodge with a pool at dusk" style="background:linear-gradient(180deg,#6a6f78 0%,#5b4a40 35%,#2f6c78 60%,#2a7c84 100%)"></div>
    <div class="shade"></div><div class="name">Project 3 name</div><div class="place">Newzeland</div>
  </a>
  <a class="project abs" style="left:483px;top:422px">
    <div class="photo" role="img" aria-label="Photo of a modern house corner with wood cladding" style="background:linear-gradient(180deg,#e6ebef 0%,#9fb2c8 35%,#4a5c80 60%,#233152 100%)"></div>
    <div class="shade"></div><div class="name">Project 6 name</div><div class="place">England</div>
  </a>
  <a class="project abs" style="left:483px;top:635px">
    <div class="photo" role="img" aria-label="Photo of a shingled house with a lit boardwalk at dusk" style="background:linear-gradient(180deg,#8db0c8 0%,#6f8fb0 40%,#4f6090 70%,#3e4a78 100%)"></div>
    <div class="shade"></div><div class="name">Project 9 name</div><div class="place">Singapore</div>
  </a>

  <div class="pager abs" style="left:194px">‹ PREV</div>
  <div class="pager abs" style="left:245px">1</div>
  <div class="pager abs" style="left:271px">····</div>
  <div class="pager abs" style="left:302px">3</div>
  <div class="pager abs" style="left:330px">4</div>
  <div class="pager-active abs"></div>
  <div class="pager pager-active-num abs" style="left:358px">5</div>
  <div class="pager abs" style="left:387px">6</div>
  <div class="pager abs" style="left:416px">7</div>
  <div class="pager abs" style="left:441px">····</div>
  <div class="pager abs" style="left:466px">94</div>
  <div class="pager abs" style="left:499px">NEXT ›</div>

  <footer class="site-footer abs"></footer>
  <div class="footer-heading abs" style="left:53px">Location &amp; Contact Info</div>
  <div class="footer-rule abs" style="left:53px"></div>
  <div class="footer-item abs" style="left:53px;top:1088px">
    <svg width="6" height="7" viewBox="0 0 6 8" style="margin-right:4px"><path d="M3 0a3 3 0 0 1 3 3c0 2-3 5-3 5S0 5 0 3a3 3 0 0 1 3-3z" fill="#f07a2c"/></svg>Some address line goes here, City name, Country name.</div>
  <div class="footer-item abs" style="left:53px;top:1105px">
    <svg width="6" height="6" viewBox="0 0 8 8" style="margin-right:4px"><path d="M1 0l2 2-1 1c.6 1.3 1.7 2.4 3 3l1-1 2 2-1.5 1C3 7.5.5 5 0 1.5z" fill="#f07a2c"/></svg>123 546 7890</div>
  <div class="footer-item abs" style="left:53px;top:1122px">
    <svg width="6" height="5" viewBox="0 0 8 6" style="margin-right:4px"><rect width="8" height="6" fill="#f07a2c"/><path d="M0 0l4 3 4-3" stroke="#262b3b" fill="none" stroke-width=".8"/></svg>info@email.com</div>

  <div class="footer-heading abs" style="left:318px">Useful Links</div>
  <div class="footer-rule abs" style="left:318px"></div>
  <div class="footer-item abs" style="left:318px;top:1088px">›&nbsp;Home</div>
  <div class="footer-item abs" style="left:318px;top:1101px">›&nbsp;Privacy Policy</div>
  <div class="footer-item abs" style="left:318px;top:1114px">›&nbsp;Terms &amp; Conditions</div>

  <div class="footer-heading abs" style="left:475px">Newsletter</div>
  <div class="footer-rule abs" style="left:475px"></div>
  <div class="news-input abs">Enter your email address...</div>
  <div class="news-button abs">
    <svg width="26" height="16" viewBox="0 0 26 16"><path d="M10 8.5l7-3.5-3 7-1-2.5z" fill="#fff"/></svg>
  </div>

  <div class="footer-divider abs"></div>
  <div class="copyright abs">© 2017, All Rights Reserved.</div>
  <div class="to-top abs">
    <svg width="24" height="24" viewBox="0 0 24 24"><path d="M12 16V8M9 11l3-3 3 3" stroke="#fff" stroke-width="1" fill="none"/></svg>
  </div>
</body>
</html>
```